Banner Ad Design Project

we are a tax resolution (help with the QRA)/accounting firm that has begun a radio campaign in south florida (am 640 and am 850). we need a banner ad, 250 x 300, that will run on the stations websites. We have a logo that can be used, check it out on our website, www.marlowfiscalaid.com. Also, we have zentrix banner ads that are running on 850 am already:

https://promo.zentrixads.example/da/b/preview?ad=1234567890&adGroup=1098765432&destinationUrl=http://book.marlowfiscalaid.com/reserve-a-session-with-a-fiscal-advisor/&height=250&hl=en_US&key=-1111222233334444555&isExpandable=false&ocid=1212343456&outputFormat=FLASH&s=61&templateId=117&visibleUrl=WWW.MARLOWFISCALAID.COM&width=300&sig=QWeRtYuIoP12-asdfGHJKLzxcvbnm0987

https://promo.zentrixads.example/da/b/preview?ad=1234567111&adGroup=1098765432&destinationUrl=http://book.marlowfiscalaid.com/reserve-a-session-with-a-fiscal-advisor/&height=250&hl=en_US&key=-6666777788889999000&isExpandable=false&ocid=1212343456&outputFormat=FLASH&s=61&templateId=24&visibleUrl=www.marlowfiscalaid.com&width=300&sig=ZxCvBnMaSd34-qwertyPLMOKNijbuhv765

we need something different and creative that will drive traffic to our site.

Thanks

```html
<!DOCTYPE html>
<html lang="en">
<head>
<meta charset="utf-8">
<title>Marlow &amp; Associates – Banner Set</title>
<link rel="stylesheet" href="https://fonts.googleapis.com/css2?family=Russo+One&family=Exo+2:wght@500&family=Cinzel:wght@600&family=Arimo:wght@700&display=swap">
<style>
  :root{
    --stage:#6e3a1e;
    --blue-top:#2a8fd6;
    --blue-bottom:#02060c;
    --orange:#e6470f;
    --purple-top:#c41fb5;
    --purple-bottom:#12020f;
    --grey-top:#ffffff;
    --grey-bottom:#9a9a9a;
    --green:#3ea632;
    --green-dark:#2b7f22;
    --gold:#efd89a;
    --ink:#141414;
    --logo:#3b3a8c;
    --rule:#6a1a6a;
  }
  *{box-sizing:border-box;margin:0;padding:0}
  html,body{width:1200px;height:1021px;overflow:hidden}
  body{background:var(--stage);position:relative}
  .banner{position:absolute;width:387px;height:323px;overflow:hidden;background:#f4f6f8}
  .banner--a{left:190px;top:165px}
  .banner--b{left:608px;top:165px}
  .banner--c{left:190px;top:521px}
  .banner--d{left:608px;top:521px}
  .photo{position:absolute;left:0;top:0;width:100%;height:190px}
  .photo--agent{background:linear-gradient(160deg,#fdfdfd 0%,#dfe6ee 45%,#9fb8d4 70%,#e9eef4 100%)}
  .photo--glasses{background:linear-gradient(120deg,#cfd9e6 0%,#a9b9cf 40%,#f1f1f1 100%)}
  .photo--couple{background:linear-gradient(110deg,#e8e2dc 0%,#d6c3b6 45%,#f3f3f3 100%)}
  .photo--relaxing{background:linear-gradient(180deg,#f7f8fa 0%,#b9cbe4 55%,#dfe5ee 100%)}
  .logo{position:absolute;right:12px;top:12px;font:700 13px/1 "Arimo",sans-serif;color:var(--logo);display:flex;align-items:center;gap:5px}
  .logo i{display:block;width:10px;height:10px;background:var(--logo)}
  .band{position:absolute;left:0;top:0;width:100%;height:100%}
  .copy{position:absolute;left:0;right:0;top:152px;text-align:center}
  .headline{font:400 31px/1 "Russo One",sans-serif;letter-spacing:1px;
    background:linear-gradient(#ffffff 0%,#e4e4e4 50%,#9a9a9a 100%);-webkit-background-clip:text;background-clip:text;color:transparent}
  .headline--orange{background:linear-gradient(#ff6a2a,#d8390a);-webkit-background-clip:text;background-clip:text}
  .subhead{font:500 28px/1.05 "Exo 2",sans-serif;color:#f2f2f2;letter-spacing:1px}
  .subhead--dark{color:var(--ink)}
  .subhead--small{font-size:24px}
  .rule{width:348px;height:1px;background:var(--rule);margin:4px auto 0}
  .tagline{margin-top:6px;font:600 15px/1.5 "Cinzel",serif;color:var(--gold)}
  .tagline b{font-size:20px;font-weight:600}
  .tagline--dark{color:var(--ink)}
  .cta{position:absolute;left:124px;top:277px;width:138px;height:41px;border-radius:4px;
    background:linear-gradient(var(--green),var(--green-dark));color:#fff;
    font:700 20px/41px "Arimo",sans-serif;text-align:center;box-shadow:0 1px 2px rgba(0,0,0,.5)}
  .cta--orange{left:230px;top:278px;background:linear-gradient(#ff5a1e,#d0330a)}
</style>
</head>
<body>

<section class="banner banner--a">
  <div class="photo photo--agent" role="img" aria-label="Smiling support agent with headset gesturing toward the viewer"></div>
  <div class="logo"><i></i>Marlow &amp; Associates</div>
  <svg class="band" viewBox="0 0 387 323" aria-hidden="true">
    <defs><linearGradient id="blueA" x1="0" y1="0" x2="0" y2="1"><stop offset="0" stop-color="#2a8fd6"/><stop offset="1" stop-color="#02060c"/></linearGradient></defs>
    <path d="M0 168 Q193 108 387 168 L387 323 L0 323Z" fill="url(#blueA)"/>
    <path d="M0 168 Q193 108 387 168" fill="none" stroke="#dfe9f4" stroke-width="3"/>
  </svg>
  <div class="copy">
    <div class="headline">GET TAX</div>
    <div class="subhead">Relief Today</div>
    <p class="tagline">It is time to get balanced and<br>handle your <b>QRA</b> issues</p>
  </div>
  <div class="cta">Click Here!</div>
</section>

<section class="banner banner--b">
  <div class="photo photo--glasses" role="img" aria-label="Relaxed smiling man in glasses leaning back with hands behind his head"></div>
  <div class="logo"><i></i>Marlow &amp; Associates</div>
  <svg class="band" viewBox="0 0 387 323" aria-hidden="true">
    <defs><linearGradient id="blueB" x1="0" y1="0" x2="0" y2="1"><stop offset="0" stop-color="#2a8fd6"/><stop offset="1" stop-color="#02060c"/></linearGradient></defs>
    <path d="M0 168 Q193 108 387 168 L387 323 L0 323Z" fill="url(#blueB)"/>
    <path d="M0 168 Q193 108 387 168" fill="none" stroke="#dfe9f4" stroke-width="3"/>
  </svg>
  <div class="copy">
    <div class="headline">GET TAX</div>
    <div class="subhead">Relief Today</div>
    <p class="tagline">It is time to get balanced and<br>handle your <b>QRA</b> issues</p>
  </div>
  <div class="cta">Click Here!</div>
</section>

<section class="banner banner--c">
  <div class="photo photo--couple" role="img" aria-label="Happy senior couple embracing"></div>
  <div class="logo"><i></i>Marlow &amp; Associates</div>
  <svg class="band" viewBox="0 0 387 323" aria-hidden="true">
    <defs><linearGradient id="greyC" x1="0" y1="0" x2="0" y2="1"><stop offset="0" stop-color="#ffffff"/><stop offset="1" stop-color="#9a9a9a"/></linearGradient></defs>
    <path d="M0 174 Q193 110 387 174 L387 323 L0 323Z" fill="url(#greyC)"/>
    <path d="M0 174 Q193 110 387 174" fill="none" stroke="#e6470f" stroke-width="5"/>
  </svg>
  <div class="copy">
    <div class="headline headline--orange">GET TAX</div>
    <div class="subhead subhead--dark">Relief Today</div>
    <div class="rule"></div>
    <p class="tagline tagline--dark">It is time to get balanced and<br>handle your <b>QRA</b> issues</p>
  </div>
  <div class="cta cta--orange">Click Here!</div>
</section>

<section class="banner banner--d">
  <div class="photo photo--relaxing" role="img" aria-label="Man seen from behind relaxing in office chair with hands behind his head"></div>
  <div class="logo"><i></i>Marlow &amp; Associates</div>
  <svg class="band" viewBox="0 0 387 323" aria-hidden="true">
    <defs><linearGradient id="purpleD" x1="0" y1="0" x2="0" y2="1"><stop offset="0" stop-color="#c41fb5"/><stop offset="1" stop-color="#12020f"/></linearGradient></defs>
    <path d="M0 168 Q193 108 387 168 L387 323 L0 323Z" fill="url(#purpleD)"/>
    <path d="M0 168 Q193 108 387 168" fill="none" stroke="#f2e4f0" stroke-width="3"/>
  </svg>
  <div class="copy">
    <div class="headline">GET RELAX</div>
    <div class="subhead subhead--small">we solve your problem</div>
    <p class="tagline">It is time to get balanced and<br>handle your <b>QRA</b> issues</p>
  </div>
  <div class="cta">Click Here!</div>
</section>

</body>
</html>
```